Expedited Project Word Template, envelopes and powerpoint template
no business card needed already have
n/a
2486 Quill Basin Lane
Norwalk, OH 44857
info@tivelmora.com
-uploaded logo needs to have ® symbol placed after the word "growing"
-already have business cards just need word template and letterhead and envelopes
-business focused on renewable energies/fresh produce production/environment, looking for classic corporate look
--trying to limit cost of printing as a start-up, so preference is for white background and then use color to highlight key areas
--powerpoint template looking for title slide, section break slide, main content slide, table slide, and image slide. template should include page numbering and private/confidential in the footer.
Here is how my biz card looks -- please note the tag line on this copy is correct"
"where technology and nature meet"

```html
<!DOCTYPE html>
<html lang="en">
<head>
<meta charset="utf-8">
<title>Tivelmora Growing – Stationery Set</title>
<link href="https://fonts.googleapis.com/css2?family=Open+Sans:wght@400;600;700&display=swap" rel="stylesheet">
<style>
  :root{
    --bg:#e9e7e3;
    --paper:#ffffff;
    --green:#86b83a;
    --teal:#5cc4d8;
    --teal-soft:#d3eef3;
    --ink:#555b60;
    --muted:#8a9095;
    --fold:#d9dcde;
  }
  *{box-sizing:border-box;margin:0;padding:0}
  html,body{width:1200px;height:550px;overflow:hidden}
  body{background:var(--bg);font-family:"Open Sans",Arial,sans-serif;color:var(--ink);position:relative}
  .sheet{position:absolute;background:var(--paper);box-shadow:0 2px 6px rgba(0,0,0,.18);overflow:hidden}
  .letterhead-first{left:24px;top:41px;width:355px;height:444px}
  .letterhead-second{left:401px;top:41px;width:355px;height:444px}
  .envelope-front{left:780px;top:41px;width:396px;height:180px}
  .envelope-back{left:780px;top:254px;width:396px;height:231px}

  .brand{display:flex;align-items:center;gap:6px}
  .brand-dot{width:14px;height:14px;border-radius:50%;background:var(--green);flex:none}
  .brand-name{font-weight:700;font-size:8.5px;letter-spacing:.3px;color:var(--green);text-transform:uppercase;line-height:1.1}
  .tagline{font-size:5px;color:var(--muted);margin-top:2px;letter-spacing:.2px}
  .brand-block{position:absolute}

  .contact-block{position:absolute;right:18px;top:14px;border-left:1px solid var(--teal);padding-left:5px;font-size:5px;line-height:1.6;color:var(--muted)}

  .watermark{position:absolute;border-radius:50%;background:var(--teal-soft);display:flex;align-items:center;justify-content:center;opacity:.85}
  .watermark span{font-weight:700;color:#ffffff;text-transform:uppercase;letter-spacing:1px}

  .footer-band{position:absolute;left:0;right:0;bottom:0;height:9px;background:var(--teal-soft)}
  .footer-band::before{content:"";position:absolute;left:0;top:0;height:9px;width:62%;background:var(--green)}
  .footer-web{position:absolute;left:50%;bottom:12px;transform:translateX(-50%);font-size:5px;color:var(--muted)}

  .footer-line{position:absolute;left:22px;right:22px;bottom:16px;display:flex;justify-content:space-between;font-size:4.6px;color:var(--muted);border-top:1px solid var(--teal);padding-top:4px}

  .envelope-flap{position:absolute;inset:0}
  .envelope-web{position:absolute;left:50%;top:40px;transform:translateX(-50%);font-size:5px;color:var(--muted)}

  .caption{position:absolute;top:506px;font-size:8px;color:var(--ink);text-align:center}
</style>
</head>
<body>

<section class="sheet letterhead-first" aria-label="Letterhead, first page">
  <div class="brand-block" style="left:18px;top:16px">
    <div class="brand"><span class="brand-dot"></span><span class="brand-name">Tivelmora Growing</span></div>
    <div class="tagline" style="margin-left:20px">where technology and nature meet</div>
  </div>
  <address class="contact-block" style="font-style:normal">
    2486 Quill Basin Lane<br>Norwalk, OH 44857<br>Tel 419 555 0142<br>info@tivelmora.com
  </address>
  <div class="watermark" style="left:92px;top:136px;width:170px;height:170px"><span style="font-size:13px">Tivelmora</span></div>
  <div class="footer-web">www.tivelmora.com</div>
  <div class="footer-band"></div>
</section>

<section class="sheet letterhead-second" aria-label="Letterhead, second page">
  <div class="brand-block" style="left:50%;top:16px;transform:translateX(-50%);text-align:center">
    <div class="brand"><span class="brand-dot"></span><span class="brand-name">Tivelmora Growing</span></div>
    <div class="tagline">where technology and nature meet</div>
  </div>
  <div class="watermark" style="left:92px;top:136px;width:170px;height:170px"><span style="font-size:13px">Tivelmora</span></div>
  <div class="footer-line">
    <span>2486 Quill Basin Lane, Norwalk, OH 44857</span>
    <span>info@tivelmora.com</span>
    <span>www.tivelmora.com</span>
  </div>
  <div class="footer-band" style="height:5px"></div>
</section>

<section class="sheet envelope-front" aria-label="Envelope, front">
  <svg class="envelope-flap" viewBox="0 0 396 180" preserveAspectRatio="none" aria-hidden="true">
    <polyline points="0,0 198,105 396,0" fill="none" stroke="var(--fold)" stroke-width="1"/>
    <polyline points="0,180 150,88" fill="none" stroke="var(--fold)" stroke-width="1"/>
    <polyline points="396,180 246,88" fill="none" stroke="var(--fold)" stroke-width="1"/>
  </svg>
  <div class="brand-block" style="left:50%;top:14px;transform:translateX(-50%)">
    <div class="brand"><span class="brand-dot"></span><span class="brand-name">Tivelmora Growing</span></div>
  </div>
  <div class="envelope-web">www.tivelmora.com</div>
</section>

<section class="sheet envelope-back" aria-label="Envelope, back">
  <div class="brand-block" style="left:16px;top:18px">
    <div class="brand"><span class="brand-dot"></span><span class="brand-name">Tivelmora Growing</span></div>
    <div class="tagline" style="margin-left:20px">where technology and nature meet</div>
  </div>
  <div class="watermark" style="left:230px;top:60px;width:120px;height:120px"><span style="font-size:9px">Tivelmora</span></div>
  <div class="footer-band" style="height:8px"></div>
</section>

<p class="caption" style="left:24px;width:355px">Letterhead page 01</p>
<p class="caption" style="left:401px;width:355px">Letterhead page 02</p>
<p class="caption" style="left:780px;width:396px">Envelope - Front &amp; Back</p>

</body>
</html>
```